Business Card Design for Mortgage Broking Business

We need to redesign the business card. Mortgage broking business, doing home loan and commercial loans, existing logo, also RQTB member logo. design style needs to be simple, professional, elegant.

once final, need to setup for a team of different names and contact details.

Industry/Entity Type

Loan

Contact Information for Business Card

Name; Mobile; Email; Address; Tel; Fax; Australian Credit Licence: 618204

```html
<!DOCTYPE html>
<html lang="en">
<head>
<meta charset="utf-8">
<title>Mortgage Broking Business – Business Card</title>
<link rel="stylesheet" href="https://fonts.googleapis.com/css2?family=Arimo:wght@400;700&family=Michroma&display=swap">
<style>
  :root {
    --bg: #2b2b2d;
    --card-white: #ffffff;
    --green-light: #4cbb48;
    --green-mid: #35a233;
    --green-dark: #1d7a1f;
    --green-band: #13691a;
    --green-text: #2e8b2e;
    --ink: #1e1e1e;
    --badge-fill: #dfe6f1;
    --partner-blue: #1f4f95;
    --white: #ffffff;
  }
  * { box-sizing: border-box; margin: 0; padding: 0; }
  html, body { width: 1200px; height: 660px; overflow: hidden; }
  body {
    background: var(--bg);
    font-family: "Arimo", Arial, sans-serif;
    position: relative;
  }
  .card {
    position: absolute;
    width: 520px;
    height: 300px;
    border-radius: 14px;
    overflow: hidden;
    box-shadow: 0 14px 30px rgba(0,0,0,.45);
  }

  /* Back: office details */
  .card-back {
    left: 50px; top: 180px;
    background: var(--card-white);
    color: var(--ink);
  }
  .office {
    position: absolute; top: 38px; left: 0; right: 0;
    text-align: center; font-size: 15px; line-height: 20px;
  }
  .office-label { font-weight: 700; }
  .rule {
    position: absolute; left: 0; right: 0; height: 1px;
    background: var(--green-mid);
  }
  .rule-top { top: 142px; }
  .rule-bottom { top: 262px; }
  .partners-label {
    position: absolute; top: 132px; left: 50%; transform: translateX(-50%);
    background: var(--card-white); padding: 0 10px;
    color: var(--green-text); font-weight: 700; font-size: 14px;
    white-space: nowrap;
  }
  .partners {
    position: absolute; top: 172px; left: 0; right: 0;
    display: flex; justify-content: center; align-items: center; gap: 50px;
  }
  .member-badge {
    width: 160px; height: 50px;
    border-radius: 4px;
    background: var(--badge-fill);
  }
  .partner-name {
    display: flex; align-items: center; gap: 8px;
    color: var(--partner-blue); font-weight: 700; font-size: 16px;
    white-space: nowrap;
  }
  .partner-name i {
    width: 14px; height: 14px; background: var(--partner-blue); display: block;
  }

  /* Front: name and brand */
  .card-front {
    left: 630px; top: 180px;
    background: linear-gradient(170deg, var(--green-light) 0%, var(--green-mid) 55%, var(--green-dark) 100%);
    color: var(--white);
  }
  .person-name {
    position: absolute; top: 20px; left: 24px;
    font-weight: 700; font-size: 17px;
  }
  .cell {
    position: absolute; top: 20px; right: 22px; font-size: 13px;
  }
  .brand {
    position: absolute; top: 78px; left: 0; right: 0; text-align: center;
  }
  .brand-name {
    font-family: "Michroma", sans-serif; font-size: 28px; letter-spacing: 1px;
    white-space: nowrap;
    text-shadow: 0 2px 3px rgba(0,0,0,.35);
  }
  .brand-sub {
    font-family: "Michroma", sans-serif; font-size: 14px;
    letter-spacing: 20px; margin-top: 4px; padding-left: 20px;
    color: rgba(255,255,255,.85);
  }
  .services {
    position: absolute; top: 180px; left: 0; right: 0; text-align: center;
    font-size: 18px;
  }
  .web-band {
    position: absolute; left: 0; right: 0; bottom: 0; height: 54px;
    background: var(--green-band);
    display: flex; align-items: center; justify-content: center;
    font-size: 15px; letter-spacing: 8px; white-space: nowrap;
  }
</style>
</head>
<body>
  <section class="card card-back" aria-label="Business card back">
    <div class="office">
      <p class="office-label">Office Address:</p>
      <p>Dummy address 4, Elm Park Road #08-03</p>
      <p>Park Building, Country - 12345</p>
      <p>E-mail : info@mortgagebroking.example</p>
    </div>
    <div class="rule rule-top"></div>
    <p class="partners-label">Our Partners/Member</p>
    <div class="partners">
      <div class="member-badge" role="img" aria-label="RQTB approved credit adviser member badge"></div>
      <div class="partner-name"><i></i>Summit Finance</div>
    </div>
    <div class="rule rule-bottom"></div>
  </section>

  <section class="card card-front" aria-label="Business card front">
    <p class="person-name">Person Name</p>
    <p class="cell">Cell.: 00000 00000</p>
    <div class="brand">
      <p class="brand-name">MORTGAGE BROKING</p>
      <p class="brand-sub">BUSINESS</p>
    </div>
    <p class="services">Home Loan and Commercial Loans</p>
    <div class="web-band">www.yourbrokersite.example</div>
  </section>
</body>
</html>
```